VORTIQ Business Card Design

We need a business card for a new company based on the Gold Coast, we are a new supplement distributing company called VORTIQ Sports Nutrition - Bold Horizon Sports Nutrition. We are providing new science based bodybuilding and fitness supplementation. Our company has a key focus towards next generation. We are wanting a card that is cool, innovative and fresh. We would like to see the implementation of the below image in a fresh and very innovative design that stands out. The final design should communicate New, Innovative, Cool, Science and researched based.
Target Market(s)
The target market is fitness and bodybuilder enthusiasts. Young audience so very cool looking.
Industry/Entity Type
Fitness
Contact Information for Business Card
(front of card)
VORTIQ Sports Nutrition.
Milo Harrow
CEO/Sport Nutrition Specialist
0473 628 904
Milo@vortiqfuelworks.example
www.vortiqfuelworks.example
(back of card)
Scientifically formulated supplement range
Private Nutrition consultations
comprehensive sports nutrition seminars
Requirements
Nice to have
- The card could have a cut out on one of the sides or one of the corners rounded off so the card looks different from a normal business card.
Should not have
- The colours need to complement each other and pop out.

```html
<!DOCTYPE html>
<html lang="en">
<head>
<meta charset="utf-8">
<title>VORTIQ Sports Nutrition – Business Card</title>
<link href="https://fonts.googleapis.com/css2?family=Open+Sans:wght@400;600;700;800&display=swap" rel="stylesheet">
<style>
  :root {
    --canvas: #2a2230;
    --card: #0b0b0c;
    --card-edge: #1a1a1c;
    --cyan: #1ab4ea;
    --cyan-light: #37c8f5;
    --white: #ffffff;
    --grey: #a9a9ad;
  }
  * { margin: 0; padding: 0; box-sizing: border-box; }
  html, body { width: 1200px; height: 800px; overflow: hidden; }
  body {
    background: var(--canvas);
    font-family: "Open Sans", Arial, sans-serif;
    display: flex;
    align-items: center;
    justify-content: center;
    gap: 60px;
  }
  .card {
    position: relative;
    width: 525px;
    height: 300px;
    background: var(--card);
    border: 1px solid var(--card-edge);
    border-radius: 4px;
    overflow: hidden;
  }

  /* Back face */
  .services {
    position: absolute;
    top: 30px;
    left: 34px;
    list-style: none;
    font-size: 13px;
    font-weight: 600;
    line-height: 24px;
    color: var(--white);
  }
  .services .highlight { color: var(--cyan); }
  .brand-large {
    position: absolute;
    right: 48px;
    top: 128px;
    display: flex;
    align-items: center;
    gap: 14px;
  }
  .brand-large .mark {
    width: 22px; height: 22px;
    border-radius: 50%;
    background: var(--cyan);
  }
  .brand-large .name {
    font-size: 64px;
    font-weight: 800;
    letter-spacing: 2px;
    color: var(--white);
    line-height: 1;
  }
  .tagline-large {
    position: absolute;
    right: 48px;
    bottom: 38px;
    font-size: 15px;
    letter-spacing: 1.5px;
    color: var(--white);
  }

  /* Front face */
  .front-band {
    position: absolute;
    inset: 0;
    width: 100%;
    height: 100%;
  }
  .brand-small {
    position: absolute;
    left: 44px;
    top: 40px;
    display: flex;
    align-items: center;
    gap: 8px;
  }
  .brand-small .mark {
    width: 12px; height: 12px;
    border-radius: 50%;
    background: var(--cyan);
  }
  .brand-small .name {
    font-size: 30px;
    font-weight: 800;
    letter-spacing: 1px;
    color: var(--white);
    line-height: 1;
  }
  .tagline-small {
    position: absolute;
    left: 44px;
    top: 80px;
    font-size: 7.5px;
    letter-spacing: 0.6px;
    color: var(--white);
  }
  .contact {
    position: absolute;
    right: 30px;
    top: 46px;
    text-align: right;
  }
  .contact .company {
    font-size: 19px;
    font-weight: 700;
    color: var(--white);
    padding-bottom: 4px;
    border-bottom: 1px solid #3a3a3e;
  }
  .contact .company .accent { color: var(--cyan); font-weight: 400; }
  .contact .person {
    margin-top: 4px;
    font-size: 11px;
    color: var(--grey);
  }
  .contact .person .role { color: var(--cyan); }
  .details {
    list-style: none;
    margin-top: 22px;
    font-size: 11.5px;
    line-height: 22px;
    color: var(--white);
  }
  .details li { display: flex; justify-content: flex-end; align-items: center; gap: 8px; }
  .details .phone-code { color: var(--cyan); }
  .details svg { width: 11px; height: 11px; flex: none; }
</style>
</head>
<body>

  <section class="card card-back" aria-label="Back of business card">
    <ul class="services">
      <li class="highlight">Scientifically formulated</li>
      <li class="highlight">supplement range</li>
      <li>Private Nutrition</li>
      <li>consultations</li>
      <li>comprehensive</li>
      <li>sports nutrition</li>
      <li>seminars</li>
    </ul>
    <div class="brand-large">
      <span class="mark"></span>
      <span class="name">VORTIQ</span>
    </div>
    <p class="tagline-large">BOLD HORIZON SPORTS NUTRITION.</p>
  </section>

  <section class="card card-front" aria-label="Front of business card">
    <svg class="front-band" viewBox="0 0 525 300" preserveAspectRatio="none" aria-hidden="true">
      <polygon points="0,168 0,300 420,300" fill="var(--cyan)"/>
      <polygon points="0,150 210,196 440,300 420,300 205,204 0,160" fill="var(--cyan-light)"/>
    </svg>
    <div class="brand-small">
      <span class="mark"></span>
      <span class="name">VORTIQ</span>
    </div>
    <p class="tagline-small">BOLD HORIZON SPORTS NUTRITION.</p>

    <div class="contact">
      <p class="company"><span class="accent">VORTIQ</span> Sports Nutrition</p>
      <p class="person">Milo Harrow <span class="role">CEO</span>/Sport Nutrition Specialist</p>
      <ul class="details">
        <li><span><span class="phone-code">(04)</span>-73-628-904</span>
          <svg viewBox="0 0 12 12"><rect x="3" y="0.5" width="6" height="11" rx="1" fill="none" stroke="var(--cyan)" stroke-width="1.2"/></svg></li>
        <li>Milo@vortiqfuelworks.example
          <svg viewBox="0 0 12 12"><rect x="1" y="2" width="10" height="8" fill="var(--cyan)"/></svg></li>
        <li>www.vortiqfuelworks.example
          <svg viewBox="0 0 12 12"><circle cx="6" cy="6" r="5" fill="var(--cyan)"/></svg></li>
      </ul>
    </div>
  </section>

</body>
</html>
```